QR248 - Plan, Guard, Track, Steer - OT Cyber Security Software, KPI Visualisation Software and

Build Website - we require a website with approx 5 tabs on scrolling pane screen - Home, Who We are, Cyber Security, Visualisation, Trusted Partners, Support, Contact, single scrolling panel or tab click to page with images and 2-3 paragraphs of text - wording and links to partners will be provided along with company logo

Target Market(s)

Process Control Markets - Oil and Gas clients, Telecommunications Operators, IOT companies, manufacturing, transport sector etc

Industry/Entity Type

Security

Coding

Coded - Design and coding required

Number of Pages Required

5+ page

Font styles to use
Sans Serif

Colors
0255a3
3176b5
85abd2
f04a50
ec1f27
1b1b1b
474747
919191
d3d3d3

Requirements
Must have
• Scrolling pane / page with tabs along the top -
• Who We are - software and professional services provider for Process Control Cyber Security and Data visualisation
• Plan Guard Track Steer -
• define and defend process control networks, measure, manage, visualise data sets from any source etc
• Process Control Cyber Security - images and wording - area for wording can be created and left to be fully populated etc
• Visualisation - data set visualisation from desk top / tablet / mobile device,
• Trusted Partners - links to www.belvanta.example www.korinex.example www.drumelo.example.au
• Support
• Contact Details
• images for cyber security risks etc
• data visualisation / visual KPI - software package
• Support - link to www.drumelo.example.au for NOC and Customer Support - sections for Gold, Silver and Bronze support package - we will add wording later
Nice to have
• Colours - blues / blacks / grey - cyber security information and sections,
• reds etc for visualisation sections
• Use similar colours as logo for rest of pages

```html
<!DOCTYPE html>
<html lang="en">
<head>
<meta charset="utf-8">
<title>QR248 – OT Cyber Security &amp; KPI Visualisation</title>
<link href="https://fonts.googleapis.com/css2?family=Roboto:wght@300;400;500;700&display=swap" rel="stylesheet">
<style>
:root{
  --blue:#0255a3;
  --blue-mid:#3176b5;
  --blue-light:#85abd2;
  --red:#f04a50;
  --red-deep:#ec1f27;
  --ink:#1b1b1b;
  --text:#474747;
  --muted:#919191;
  --line:#d3d3d3;
  --white:#ffffff;
}
*{box-sizing:border-box;margin:0;padding:0}
html,body{width:1200px;height:3614px;overflow:hidden}
body{font-family:'Roboto',Arial,sans-serif;color:var(--text);background:var(--white);position:relative}
h1,h2,h3,h4{font-weight:400}
.abs{position:absolute}

/* nav */
.site-nav{position:absolute;top:0;left:0;width:1200px;height:72px;background:var(--white);border-bottom:1px solid var(--line)}
.brand{position:absolute;left:85px;top:20px;display:flex;align-items:center;gap:12px;font-size:25px;font-weight:500;color:var(--ink)}
.brand-mark{width:30px;height:30px;border:5px solid var(--red-deep);border-radius:4px}
.nav-links{position:absolute;right:80px;top:0;display:flex;height:72px;list-style:none}
.nav-links li{padding:0 17px;line-height:72px;font-size:16px;color:var(--ink)}
.nav-links li.active{background:var(--blue);color:var(--white)}

/* hero */
.hero{top:72px;left:0;width:1200px;height:528px;background:radial-gradient(ellipse at 50% 40%,#5a6068 0%,#2b2f35 55%,#141619 100%)}
.hero-title{top:290px;width:1200px;text-align:center;color:var(--white);font-size:44px;font-weight:700;letter-spacing:.5px}
.hero-sub{top:347px;width:1200px;text-align:center;color:var(--white);font-size:29px;font-weight:400}

/* who */
.who-title{top:655px;width:1200px;text-align:center;font-size:34px;color:var(--ink)}
.who-text{top:712px;left:100px;width:1000px;text-align:center;font-size:13.5px;line-height:25px}

/* product */
.prod-title{left:85px;top:872px;font-size:30px;color:var(--ink)}
.prod-sub{left:85px;top:918px;font-size:14px;font-weight:700;color:var(--ink)}
.prod-badge{left:92px;top:962px;width:86px;height:86px;border-radius:50%;background:#e6eef7}
.prod-lead{left:220px;top:975px;width:400px;font-size:13.5px;line-height:22px}
.prod-text{left:85px;top:1090px;width:540px;font-size:13.5px;line-height:22px}
.pillar{width:215px;height:182px;background:var(--blue);color:var(--white);text-align:center;padding-top:14px}
.pillar svg{width:42px;height:42px}
.pillar h3{font-size:17px;font-weight:500;margin:6px 0 8px}
.pillar p{font-size:11.5px;line-height:17px;padding:0 16px}

/* process control */
.rig-photo{top:1275px;left:0;width:600px;height:520px;background:linear-gradient(180deg,#f2f2f2 0%,#bdbdbd 55%,#6f6f6f 80%,#e9e9e9 100%)}
.pc-title{left:636px;top:1335px;font-size:27px;color:var(--ink)}
.red-rule{height:2px;width:60px;background:var(--red)}
.pc-text{left:636px;width:500px;font-size:13px;line-height:21px}
.pc-feature{width:160px;text-align:center;font-size:13.5px;line-height:21px;color:var(--ink)}
.pc-icon{width:68px;height:68px;border:1px solid var(--line);border-radius:50%;margin:0 auto 16px;display:flex;align-items:center;justify-content:center}

/* kpi */
.kpi-brand{left:85px;top:1855px;font-size:22px;font-weight:700;color:var(--red-deep)}
.kpi-title{left:85px;top:1890px;font-size:33px;color:var(--ink)}
.kpi-text{left:85px;top:1950px;width:490px;font-size:13px;line-height:21px}
.kpi-card{width:235px;height:90px;background:var(--blue-light);color:var(--white);padding:14px 16px}
.kpi-card h4{font-size:16px;font-weight:500;margin-bottom:6px}
.kpi-card p{font-size:11.5px;line-height:16px}
.chart-shot{top:1800px;left:600px;width:598px;height:545px;border:2px solid var(--line);background:linear-gradient(180deg,#f4f6f9 0%,#e9eef5 100%)}

/* partners */
.partners{top:2410px;left:0;width:1200px;height:300px;background:radial-gradient(ellipse at 50% 60%,#1d3040 0%,#0d141b 70%,#080b0e 100%)}
.partners-title{top:2465px;width:1200px;text-align:center;font-size:27px;color:var(--white);font-weight:500}
.partner{top:2565px;display:flex;align-items:center;gap:14px;font-size:34px;font-weight:500;color:var(--white)}
.partner-dot{width:40px;height:40px;border-radius:50%;background:var(--muted)}

/* support */
.support-art{top:2770px;left:0;width:495px;height:410px;background:radial-gradient(circle at 45% 45%,#45c4d4 0%,#2bb3c6 55%,#1f9fb2 100%)}
.support-label{top:3125px;left:0;width:495px;text-align:center;color:var(--white);font-size:24px;letter-spacing:1px}
.support-title{left:540px;top:2827px;font-size:27px;color:var(--ink);font-weight:500}
.support-text{left:540px;width:560px;font-size:13.5px;line-height:22px}
.btn{left:540px;top:3055px;width:132px;height:44px;background:var(--blue);color:var(--white);font-size:15px;display:flex;align-items:center;justify-content:center}

/* contact */
.contact{top:3240px;left:0;width:1200px;height:315px;background:linear-gradient(180deg,#eef2f5 0%,#f7f9fa 100%)}
.contact-title{top:3280px;width:1200px;text-align:center;font-size:27px;color:var(--ink);font-weight:700}
.contact-item{top:3370px;display:flex;align-items:flex-start;gap:12px;font-size:15px;line-height:20px;color:var(--ink)}
.contact-item.big{font-size:21px;line-height:36px}
.contact-pin{width:36px;height:36px;background:var(--red);transform:rotate(45deg);flex:none;display:flex;align-items:center;justify-content:center;margin-top:2px}
.contact-pin svg{transform:rotate(-45deg)}
.contact-foot{top:3440px;width:1200px;text-align:center;font-size:17px;line-height:27px;color:var(--ink)}

/* footer */
.site-footer{top:3555px;left:0;width:1200px;height:59px;background:#1f1f1f}
.copy{left:85px;top:3576px;font-size:12px;color:#cfcfcf}
.social{top:3572px;width:24px;height:24px;background:var(--red-deep);border-radius:3px}
</style>
</head>
<body>

<nav class="site-nav">
  <div class="brand"><span class="brand-mark"></span>Logo Here</div>
  <ul class="nav-links">
    <li class="active">Home</li><li>Who We are</li><li>Cyber Security</li><li>Visualisation</li><li>Trusted Partners</li><li>Support</li><li>Contact</li>
  </ul>
</nav>

<section class="abs hero" role="img" aria-label="Dark photo of a hand touching a glowing network of connected icons"></section>
<h1 class="abs hero-title">YOUR NETWORK</h1>
<p class="abs hero-sub">AND YOUR DATA IS YOUR BUSINESS</p>

<h2 class="abs who-title">Who We are</h2>
<p class="abs who-text">Sed ut perspiciatis unde omnis iste natus error sit voluptatem accusantium doloremque laudantium, totam rem aperiam, eaque ipsa quae ab illo inventore veritatis et quasi architecto beatae vitae dicta sunt explicabo. Nemo enim ipsam voluptatem quia voluptas sit aspernatur aut odit aut fugit, sed quia consequuntur magni dolores eos qui ratione voluptatem sequi nesciunt. Neque porro quisquam est, qui dolorem ipsum</p>

<h2 class="abs prod-title">QR248 enables you to do that</h2>
<p class="abs prod-sub">Plan, Guard, Track, Steer – 365 days a year</p>
<div class="abs prod-badge" role="img" aria-label="QR248 product badge"></div>
<p class="abs prod-lead">Defending that data, the network on which you move that data and understanding what that data is telling you is key to the success of every business.</p>
<p class="abs prod-text">Sed ut perspiciatis unde omnis iste natus error sit voluptatem accusantium doloremque laudantium, totam rem aperiam, eaque ipsa quae ab illo inventore veritatis et quasi architecto beatae vitae dicta sunt explicabo.</p>

<div class="abs pillar" style="left:675px;top:836px">
  <svg viewBox="0 0 42 42" fill="none" stroke="#fff" stroke-width="2"><circle cx="21" cy="18" r="9"/><path d="M17 28h8M18 32h6M21 3v4M7 18H3M39 18h-4M10 7l3 3M32 7l-3 3"/></svg>
  <h3>Plan</h3><p>Baseline your OT communications with passive capture of your assets know your topology with confidence</p>
</div>
<div class="abs pillar" style="left:900px;top:836px">
  <svg viewBox="0 0 42 42" fill="none" stroke="#fff" stroke-width="2"><path d="M21 4l14 5v10c0 9-6 15-14 19C13 34 7 28 7 19V9z"/><path d="M21 4v34"/></svg>
  <h3>Guard</h3><p>Baseline your OT communications with passive capture of your assets know your topology with confidence</p>
</div>
<div class="abs pillar" style="left:675px;top:1030px">
  <svg viewBox="0 0 42 42" fill="none" stroke="#fff" stroke-width="2"><rect x="4" y="15" width="34" height="12" rx="1"/><path d="M10 15v5M16 15v4M22 15v5M28 15v4M34 15v5"/></svg>
  <h3>Track</h3><p>Baseline your OT communications with passive capture of your assets know your topology with confidence</p>
</div>
<div class="abs pillar" style="left:900px;top:1030px">
  <svg viewBox="0 0 42 42" fill="none" stroke="#fff" stroke-width="2"><path d="M5 12h32M5 21h32M5 30h32"/><circle cx="14" cy="12" r="3" fill="#0255a3"/><circle cx="27" cy="21" r="3" fill="#0255a3"/><circle cx="18" cy="30" r="3" fill="#0255a3"/></svg>
  <h3>Steer</h3><p>Baseline your OT communications with passive capture of your assets know your topology with confidence</p>
</div>

<section class="abs rig-photo" role="img" aria-label="Black and white photo of an offshore oil platform"></section>
<h2 class="abs pc-title">Process Control Cyber Security</h2>
<div class="abs red-rule" style="left:636px;top:1378px"></div>
<p class="abs pc-text" style="top:1395px">Sed ut perspiciatis unde omnis iste natus error sit voluptatem accusantium doloremque laudantium, totam rem aperiam, eaque ipsa quae ab illo inventore veritatis et quasi architecto beatae vitae dicta sunt explicabo. Nemo enim ipsam voluptatem quia voluptas</p>
<p class="abs pc-text" style="top:1500px">sit aspernatur aut odit aut fugit, sed quia consequuntur magni dolores eos qui ratione ipsam voluptatem quia voluptas</p>
<div class="abs pc-feature" style="left:636px;top:1585px">
  <div class="pc-icon"><svg width="30" height="30" viewBox="0 0 30 30" fill="none" stroke="#0255a3" stroke-width="2"><rect x="4" y="4" width="22" height="22" rx="2"/><circle cx="15" cy="13" r="4"/><path d="M9 23c1-4 11-4 12 0"/></svg></div>
  Sed ut perspiciatis un de omnis iste
</div>
<div class="abs pc-feature" style="left:796px;top:1585px">
  <div class="pc-icon"><svg width="30" height="30" viewBox="0 0 30 30" fill="none" stroke="#0255a3" stroke-width="2"><rect x="7" y="13" width="16" height="13" rx="1"/><path d="M10 13V9a5 5 0 0 1 10 0v4"/><circle cx="15" cy="19" r="2"/></svg></div>
  Sed ut perspiciatis un de omnis iste
</div>
<div class="abs pc-feature" style="left:956px;top:1585px">
  <div class="pc-icon"><svg width="30" height="30" viewBox="0 0 30 30" fill="none" stroke="#0255a3" stroke-width="2"><rect x="11" y="3" width="8" height="7"/><rect x="3" y="20" width="8" height="7"/><rect x="19" y="20" width="8" height="7"/><path d="M15 10v5M7 20v-5h16v5"/></svg></div>
  Sed ut perspiciatis un de omnis iste
</div>

<p class="abs kpi-brand">ChartLume</p>
<h2 class="abs kpi-title">KPI Visualisation</h2>
<div class="abs red-rule" style="left:85px;top:1937px"></div>
<p class="abs kpi-text">Sed ut perspiciatis unde omnis iste natus error sit voluptatem accusantium doloremque laudantium, totam rem aperiam, eaque ipsa quae ab illo inventore veritatis et quasi architecto beatae vitae dicta sunt explicabo. Nemo enim ipsam voluptatem quia voluptas</p>
<div class="abs kpi-card" style="left:85px;top:2060px"><h4>Read Data in Real-Time</h4><p>Leave your data where it makes sense and read</p></div>
<div class="abs kpi-card" style="left:333px;top:2060px"><h4>Simplify by Adding Context</h4><p>Transform raw data into intuitive KPIs everyone can understand...</p></div>
<div class="abs kpi-card" style="left:85px;top:2164px"><h4>Read Data in Real-Time</h4><p>Leave your data where it makes sense and read</p></div>
<div class="abs kpi-card" style="left:333px;top:2164px"><h4>Simplify by Adding Context</h4><p>Transform raw data into intuitive KPIs everyone can understand...</p></div>

<section class="abs chart-shot" role="img" aria-label="Screenshot of the KPI software showing a fuel cost trend chart"></section>

<section class="abs partners" role="img" aria-label="Dark blue background with a faint network pattern"></section>
<h2 class="abs partners-title">Trusted Partners</h2>
<div class="abs partner" style="left:165px"><span class="partner-dot"></span>Belvanta</div>
<div class="abs partner" style="left:440px"><span class="partner-dot"></span>Korinex</div>
<div class="abs partner" style="left:818px"><span class="partner-dot"></span>Drumelo</div>

<section class="abs support-art" role="img" aria-label="Illustration of a support agent with a headset surrounded by contact icons"></section>
<p class="abs support-label">SUPPORT</p>
<h2 class="abs support-title">Customer Support</h2>
<div class="abs red-rule" style="left:540px;top:2863px"></div>
<p class="abs support-text" style="top:2880px">NOC and Customer Support Sed ut perspiciatis unde omnis iste natus error sit voluptatem accusantium doloremque laudantium, totam rem aperiam, eaque ipsa quae ab illo inventore veritatis et quasi architecto beatae vitae dicta sunt explicabo.</p>
<p class="abs support-text" style="top:2977px">Nemo enim ipsam voluptatem quia architecto beatae vitae dicta sunt explicabo. Nemo enim ipsam voluptatem quia</p>
<div class="abs btn">Get Support</div>

<section class="abs contact" role="img" aria-label="Pale blurred office background"></section>
<h2 class="abs contact-title">Contact Details</h2>
<div class="abs red-rule" style="left:570px;top:3320px"></div>
<div class="abs contact-item" style="left:200px">
  <span class="contact-pin"><svg width="16" height="16" viewBox="0 0 16 16" fill="#fff"><path d="M8 1a5 5 0 0 0-5 5c0 4 5 9 5 9s5-5 5-9a5 5 0 0 0-5-5zm0 7a2 2 0 1 1 0-4 2 2 0 0 1 0 4z"/></svg></span>
  <span>88 Fenwick St., Suite 410<br>Toronto, ON M4K 1A2<br>Canada</span>
</div>
<div class="abs contact-item big" style="left:505px">
  <span class="contact-pin"><svg width="16" height="16" viewBox="0 0 16 16" fill="#fff"><path d="M4 1l3 3-2 2c1 2 3 4 5 5l2-2 3 3-2 3C7 15 1 9 1 3z"/></svg></span>
  <span>555 - 014 - 8221</span>
</div>
<div class="abs contact-item" style="left:760px;top:3378px">
  <span class="contact-pin"><svg width="16" height="16" viewBox="0 0 16 16" fill="none" stroke="#fff" stroke-width="1.6"><rect x="2" y="4" width="12" height="9"/><path d="M2 4l6 5 6-5"/></svg></span>
  <span style="margin-top:8px">info@qr248.example</span>
</div>
<p class="abs contact-foot">Contact<br>QR248 today and be in control tomorrow</p>

<footer class="abs site-footer"></footer>
<p class="abs copy">Copyright © 2018. All rights reserved.</p>
<span class="abs social" style="left:1008px"></span>
<span class="abs social" style="left:1042px"></span>
<span class="abs social" style="left:1076px"></span>

</body>
</html>
```